Postcard For neighbors near worksite

We are a residential interior and exterior painting company. I will be sending post cards out in neighborhoods that we will be currently working in. Basically giving the neighbors a "Neighborhood Notice" that we are in the area and would like to give a Free Estimate to anyone in that neighborhood. I will attach a file of another companies idea that I like. Also, I attached my Logo. Brightcoat Painting & More

Target Market(s)

Neighbors near where we are working

Industry/Entity Type

It Company

Requirements
Must have
• Website: Brightcoatpaint.example
• Number: 555.204.6617

```html
<!DOCTYPE html>
<html lang="en">
<head>
<meta charset="utf-8">
<title>Brightcoat Painting &amp; More – Neighborhood Notice Postcard</title>
<link href="https://fonts.googleapis.com/css2?family=Roboto+Condensed:ital,wght@0,400;0,700;1,700&family=Roboto:wght@400&display=swap" rel="stylesheet">
<style>
  :root {
    --brand-red: #e41e25;
    --tail-red: #a8141a;
    --ink: #111111;
    --paper: #ffffff;
    --footer: #1d1d1d;
    --backdrop: #eeeeee;
  }
  * { margin: 0; padding: 0; box-sizing: border-box; }
  html, body { width: 1200px; height: 1200px; overflow: hidden; background: var(--backdrop); }
  .postcard {
    position: absolute; left: 283px; top: 30px;
    width: 634px; height: 1140px;
    background: var(--paper); overflow: hidden;
    font-family: "Roboto", Arial, sans-serif; color: var(--ink);
  }
  .header { position: absolute; left: 0; top: 0; width: 100%; height: 151px; }
  .brand-name {
    position: absolute; left: 62px; top: 48px; width: 190px;
    font-family: "Roboto Condensed", Arial, sans-serif; font-weight: 700;
    font-size: 27px; line-height: 1.05; color: var(--brand-red);
  }
  .services-kicker {
    position: absolute; left: 274px; top: 59px; width: 316px;
    font-family: "Roboto Condensed", Arial, sans-serif; font-size: 15.5px;
    letter-spacing: 0.1px; white-space: nowrap;
  }
  .services-title {
    position: absolute; left: 271px; top: 75px;
    font-family: "Roboto Condensed", Arial, sans-serif; font-weight: 700;
    font-size: 47px; line-height: 1; color: var(--brand-red); white-space: nowrap;
    transform: scaleX(0.88); transform-origin: left top;
  }
  .hero-photo {
    position: absolute; left: 0; top: 151px; width: 100%; height: 361px;
    background: linear-gradient(180deg, #b9d6ec 0%, #d7e3ea 30%, #c9b79a 55%, #8f7a66 72%, #6f8f4f 88%, #b9b7b1 100%);
  }
  .notice-banner { position: absolute; left: 0; top: 0; width: 634px; height: 1140px; pointer-events: none; }
  .notice-banner text { font-family: "Roboto Condensed", Arial, sans-serif; fill: var(--paper); }
  .promise {
    position: absolute; left: 0; top: 547px; width: 100%;
    text-align: center; font-family: "Roboto Condensed", Arial, sans-serif;
    font-style: italic; font-weight: 700; font-size: 20px; line-height: 24px;
  }
  .service-band { position: absolute; background: var(--brand-red); }
  .service-photo { position: absolute; }
  .band-interior { left: 405px; top: 612px; width: 229px; height: 137px; }
  .photo-interior { left: 412px; top: 619px; width: 167px; height: 125px;
    background: linear-gradient(135deg, #dfe6e2 0%, #9fb7a8 45%, #f2f2ee 70%, #6d6152 100%); }
  .band-exterior { left: 0; top: 759px; width: 225px; height: 137px; }
  .photo-exterior { left: 52px; top: 766px; width: 167px; height: 125px;
    background: linear-gradient(90deg, #b9c68f 0%, #e3e6d5 35%, #9a2428 60%, #f1efe9 80%, #7b1d20 100%); }
  .service-copy { position: absolute; font-size: 19px; line-height: 23.6px; }
  .service-copy h2 { font-weight: 400; font-size: 24.5px; line-height: 28px; margin-bottom: 1px; }
  .copy-interior { right: 246px; top: 617px; width: 360px; text-align: right; }
  .copy-exterior { left: 248px; top: 766px; width: 360px; }
  .guarantee {
    position: absolute; left: 0; top: 910px; width: 100%; text-align: center;
    font-family: "Roboto Condensed", Arial, sans-serif; font-style: italic; font-weight: 700;
    font-size: 25px; line-height: 28px; color: var(--brand-red);
  }
  .call-label {
    position: absolute; left: 66px; top: 944px;
    font-family: "Roboto Condensed", Arial, sans-serif; font-size: 27px; line-height: 26px;
  }
  .call-label .now { display: block; padding-left: 20px; font-weight: 700; font-style: italic; font-size: 33px; line-height: 30px; }
  .phone {
    position: absolute; left: 185px; top: 935px;
    font-family: "Roboto Condensed", Arial, sans-serif; font-size: 73px; line-height: 1; white-space: nowrap;
  }
  .footer {
    position: absolute; left: 0; top: 1021px; width: 100%; height: 119px;
    background: var(--footer); color: var(--paper); text-align: center;
    font-family: "Roboto Condensed", Arial, sans-serif; font-size: 44px; line-height: 78px;
  }
</style>
</head>
<body>
<main class="postcard">
  <header class="header">
    <div class="brand-name">Brightcoat Painting &amp; More</div>
    <div class="services-kicker">PROFESSIONAL RESIDENTIAL AND COMMERCIAL</div>
    <div class="services-title">PAINTING SERVICES</div>
  </header>

  <div class="hero-photo" role="img" aria-label="Photo of a large two-storey craftsman house with fresh paint, white garage door and green trees"></div>

  <svg class="notice-banner" viewBox="0 0 732 1317" preserveAspectRatio="none">
    <polygon points="491,624 646,577 556,592" fill="var(--tail-red)"/>
    <polygon points="76,487 644,442 649,574 81,622" fill="var(--brand-red)"/>
    <g transform="rotate(-4.6 96 540)">
      <text x="96" y="540" font-size="60" font-weight="700" textLength="528" lengthAdjust="spacingAndGlyphs">NEIGHBORHOOD NOTICE!</text>
      <text x="100" y="594" font-size="54" font-weight="700" textLength="266" lengthAdjust="spacingAndGlyphs">FREE ESTIMATE</text>
      <text x="386" y="570" font-size="21" font-weight="400">TO ANYONE IN</text>
      <text x="386" y="596" font-size="21" font-weight="400">THAT NEIGHBORHOOD</text>
    </g>
  </svg>

  <p class="promise">We maintain the highest quality of industry standards and stand<br>behind our work 100 percent, helping you avoid costly problems.</p>

  <div class="service-band band-interior"></div>
  <div class="service-photo photo-interior" role="img" aria-label="Photo of a freshly painted kitchen interior with tall shuttered windows"></div>
  <section class="service-copy copy-interior">
    <h2>INTERIOR PAINTING</h2>
    <p>Does the look of your home or<br>apartment need revitalized?<br>Let our painting contractors transform<br>the look of your home’s interior.</p>
  </section>

  <div class="service-band band-exterior"></div>
  <div class="service-photo photo-exterior" role="img" aria-label="Photo of a painted front porch with red double doors and a porch swing"></div>
  <section class="service-copy copy-exterior">
    <h2>EXTERIOR PAINTING</h2>
    <p>Add value and curb appeal to your<br>home or business with our exterior<br>painting services. We do house<br>painting and much more.</p>
  </section>

  <p class="guarantee">Beauty and Peace of Mind – 100% Guaranteed</p>
  <div class="call-label">CALL US<span class="now">NOW</span></div>
  <div class="phone">555.204.6617</div>

  <footer class="footer">www.Brightcoatpaint.example</footer>
</main>
</body>
</html>
```